Business card for femtech company

Nothing too elaborate but elegant and geared towards the mother and baby market. Prefer full-bleed with logo (attached) rear.

```html
<!DOCTYPE html>
<html lang="en">
<head>
<meta charset="utf-8">
<title>Nestwell business card</title>
<link rel="stylesheet" href="https://fonts.googleapis.com/css2?family=Montserrat:wght@400;700&family=Arimo:wght@400&display=swap">
<style>
  :root {
    --bg: #1f1f21;
    --card: #f6f6f5;
    --teal: #5bbfb3;
    --grey: #9b9b9b;
    --ink: #1c1c1c;
    --rule: #b9b9b9;
  }
  * { box-sizing: border-box; margin: 0; padding: 0; }
  html, body { width: 1200px; height: 960px; overflow: hidden; }
  body {
    background: var(--bg);
    display: flex;
    flex-direction: column;
    align-items: center;
    justify-content: center;
    gap: 40px;
  }
  .card {
    width: 700px;
    height: 400px;
    background: var(--card);
    border-radius: 22px;
    position: relative;
  }
  .card-back {
    display: flex;
    align-items: center;
    justify-content: center;
    gap: 22px;
  }
  .back-mark {
    width: 120px;
    height: 120px;
    border-radius: 50%;
    background: var(--teal);
  }
  .back-name {
    font-family: "Montserrat", sans-serif;
    font-weight: 400;
    font-size: 54px;
    color: var(--teal);
    letter-spacing: 1px;
  }
  .card-front {
    display: flex;
    align-items: center;
    padding: 0 60px;
  }
  .brand {
    display: flex;
    align-items: center;
    gap: 18px;
    width: 290px;
  }
  .brand-dot {
    width: 52px;
    height: 52px;
    border-radius: 50%;
    background: var(--teal);
  }
  .brand-name {
    font-family: "Montserrat", sans-serif;
    font-weight: 400;
    font-size: 38px;
    color: var(--grey);
    letter-spacing: 1px;
  }
  .divider {
    width: 1px;
    height: 190px;
    background: var(--rule);
    margin-right: 26px;
  }
  .contact { font-family: "Arimo", sans-serif; color: var(--ink); }
  .person-name {
    font-family: "Montserrat", sans-serif;
    font-weight: 700;
    font-size: 26px;
    color: var(--teal);
    line-height: 1;
  }
  .person-role {
    font-size: 17px;
    color: var(--grey);
    margin: 4px 0 14px;
  }
  .address { font-size: 19px; line-height: 1.25; margin-bottom: 10px; }
  .line {
    display: flex;
    align-items: center;
    gap: 10px;
    font-size: 19px;
    line-height: 1.3;
  }
  .line svg { width: 14px; height: 14px; fill: var(--teal); flex: none; }
</style>
</head>
<body>
  <section class="card card-back">
    <div class="back-mark"></div>
    <span class="back-name">nestwell</span>
  </section>

  <section class="card card-front">
    <div class="brand">
      <div class="brand-dot"></div>
      <span class="brand-name">nestwell</span>
    </div>
    <div class="divider"></div>
    <div class="contact">
      <p class="person-name">Elena Marsh</p>
      <p class="person-role">President</p>
      <p class="address">27 Linden Row<br>Maple Grove, NY 10020</p>
      <p class="line">
        <svg viewBox="0 0 16 16" aria-hidden="true"><path d="M3.6 1.2l2.3 2.9-1.3 1.6c.9 2 2.6 3.7 4.7 4.7l1.6-1.3 2.9 2.3-1.5 2.2C7.5 13.4 2.6 8.5 1.4 2.7z"/></svg>
        (555) 0142-7788
      </p>
      <p class="line">
        <svg viewBox="0 0 16 16" aria-hidden="true"><path d="M1 3h14v10H1zM2 4.2v.5l6 4 6-4v-.5z"/></svg>
        hello@nestwell.com
      </p>
      <p class="line">
        <svg viewBox="0 0 16 16" aria-hidden="true"><circle cx="8" cy="8" r="7"/></svg>
        www.nestwell.com
      </p>
    </div>
  </section>
</body>
</html>
```